Bright Towns Alliance PowerPoint Design Template and Sample Deck

The Bright Towns Alliance is an international organization that seeks to improve the livability, workability and sustainability of the world’s cities.
We seek a versatile PowerPoint design template with 10 slide types plus a “self-documenting” sample deck. Your design will be used in keynote speeches and workshops around the world.
After the contest is completed, we will ask the winning designer to add 10-20 additional slide types for $75 per slide. We also seek a long-term relationship whereby we can request “custom” slides and/or ask the designer to touch up the slides we build to make them better.
FILES. We have uploaded several files:
1. BRIGHT TOWNS ALLIANCE DESIGN CONTEST NOTES.docx with full instructions.
2. PALETTE. Shows our official colors.
3 LOGOS. Several individual files with different variations of our logo. Some with our motto, some without.
2. SAMPLE SLIDES. Because we were unable to successfully upload our sample deck, we are making it available via this FileCrate link:
https://www.filecrate-example.net/s/k7qvmr2tn8wzd4h/The%20Bright%20Towns%20Alliance%20Design%20Contest%20Notes.docx?dl=0
Target Market(s)
Mayors, department heads, CIOs, senior executives from technology companies
Industry/Entity Type
Information Technology
Colors
Designer to choose colors to be used in the design.
Requirements
Must have
- Please see uploaded Word document for requirements, nice to haves and should not haves and uploaded palette for color preferences.
Nice to have
- see above
Should not have
- see above

```html
<!DOCTYPE html>
<html lang="en">
<head>
<meta charset="utf-8">
<title>Bright Towns Alliance — Presentation Template</title>
<link rel="stylesheet" href="https://fonts.googleapis.com/css2?family=Questrial&display=swap">
<style>
:root{
  --navy:#1c3468;
  --blue:#2a66d0;
  --sky:#3a86e8;
  --orange:#f28a1e;
  --slate:#3f5f93;
  --slate-dark:#2a4778;
  --ink:#3b3f4a;
  --muted:#8a8f99;
  --rule:#c9d3e3;
  --paper:#ffffff;
  --page:#ffffff;
}
*{box-sizing:border-box;margin:0;padding:0}
html,body{width:1200px;height:2961px;overflow:hidden;background:var(--page)}
body{position:relative;font-family:"Questrial",Arial,sans-serif;color:var(--ink)}
.slide{position:absolute;width:560px;height:314px;background:var(--paper);overflow:hidden;
  box-shadow:0 3px 8px rgba(0,0,0,.28)}
.col-a{left:26px}.col-b{left:614px}
.dark{background:linear-gradient(135deg,var(--slate) 0%,var(--slate-dark) 100%);color:#fff}
.abs{position:absolute}
.photo{position:absolute}
.body-text{font-size:5.6px;line-height:1.45;color:var(--ink)}
.dark .body-text{color:#e8eefa}
.head{position:absolute;left:26px;top:18px;font-size:16px;color:var(--blue);display:flex;align-items:center;gap:8px}
.head .mark{width:9px;height:9px;background:var(--navy)}
.brand-stack{position:absolute;left:14px;bottom:12px;font-size:7px;line-height:1.05;color:var(--navy)}
.brand-dot{position:absolute;right:14px;bottom:12px;width:12px;height:12px;background:var(--navy)}
.dark .brand-stack{font-size:15px;color:#fff}
.orange-title{color:var(--orange);font-size:24px;line-height:1.1}
.caption{font-size:6px;color:var(--navy);text-align:center}
.timeline-year{position:absolute;font-size:19px;color:var(--navy)}
.social{display:flex;gap:3px;justify-content:center}
.social span{width:11px;height:11px;background:var(--blue)}
.social span:nth-child(2){background:var(--sky)}
.social span:nth-child(4){background:#6aa83a}
.agenda-item{display:flex;align-items:center;gap:14px;font-size:8px;color:var(--navy)}
.agenda-item span{width:9px;height:9px;background:var(--navy)}
</style>
</head>
<body>

<!-- 1 Cover -->
<section class="slide col-a" style="top:34px">
  <div class="photo" role="img" aria-label="Collage of city and technology photographs in blue and orange tones" style="left:18px;top:8px;width:250px;height:290px;background:linear-gradient(160deg,#c9d2dc 0%,#6f8fc0 45%,#1c3468 80%,#3d5f96 100%)"></div>
  <div class="abs" style="left:300px;top:66px;font-size:22px;color:var(--blue)">Lorem ipsum dolor</div>
  <div class="abs body-text" style="left:380px;top:96px;width:160px">Lorem ipsum dolor sit amet, consetetur sadipscing elitr, sed diam nonumy eirmod tempor invidunt ut labore et dolore magna.</div>
  <div class="abs" style="right:20px;bottom:14px;font-size:13px;color:var(--navy)">Bright Towns Alliance</div>
</section>

<!-- 2 Agenda -->
<section class="slide col-b" style="top:34px">
  <div class="head" style="font-size:15px;color:var(--navy)"><span class="mark"></span>Agenda</div>
  <div class="abs" style="left:192px;top:0;width:1px;height:314px;background:var(--rule)"></div>
  <div class="abs" style="left:186px;top:74px;width:13px;height:13px;background:var(--navy)"></div>
  <div class="abs" style="left:214px;top:73px;font-size:12px;color:var(--navy)">Lorem Ipsum Dolor Sit Amet</div>
  <div class="abs" style="left:188px;top:118px;display:flex;flex-direction:column;gap:24px">
    <div class="agenda-item"><span></span>Lorem Ipsum Dolor Sit Amet</div>
    <div class="agenda-item"><span></span>Lorem Ipsum Dolor Sit Amet</div>
    <div class="agenda-item"><span></span>Lorem Ipsum Dolor Sit Amet</div>
    <div class="agenda-item"><span></span>Lorem Ipsum Dolor Sit Amet</div>
    <div class="agenda-item"><span></span>Lorem Ipsum Dolor Sit Amet</div>
  </div>
  <div class="brand-stack">Bright<br>Towns<br>Alliance</div><div class="brand-dot"></div>
</section>

<!-- 3 Text and photo -->
<section class="slide col-a" style="top:388px">
  <div class="head"><span class="mark"></span>Lorem ipsum</div>
  <p class="abs body-text" style="left:26px;top:50px;width:250px">Lorem ipsum dolor sit amet, consetetur sadipscing elitr, sed diam nonumy eirmod tempor invidunt ut labore et dolore magna aliquyam erat, sed diam voluptua. At vero eos et accusam et justo duo dolores et ea rebum.</p>
  <div class="abs" style="left:60px;top:112px;display:flex;flex-direction:column;gap:26px;width:200px">
    <div><div style="display:flex;gap:6px;align-items:center;font-size:7px;color:var(--navy)"><span style="width:6px;height:6px;background:var(--navy)"></span>Lorem Ipsum Dolor Sit Amet</div><p class="body-text" style="padding-left:12px;margin-top:3px">Lorem ipsum dolor sit amet, consetetur sadipscing elitr, sed diam nonumy eirmod tempor.</p></div>
    <div><div style="display:flex;gap:6px;align-items:center;font-size:7px;color:var(--navy)"><span style="width:6px;height:6px;background:var(--navy)"></span>Lorem Ipsum Dolor Sit Amet</div><p class="body-text" style="padding-left:12px;margin-top:3px">Lorem ipsum dolor sit amet, consetetur sadipscing elitr, sed diam nonumy eirmod tempor.</p></div>
    <div><div style="display:flex;gap:6px;align-items:center;font-size:7px;color:var(--navy)"><span style="width:6px;height:6px;background:var(--navy)"></span>Lorem Ipsum Dolor Sit Amet</div><p class="body-text" style="padding-left:12px;margin-top:3px">Lorem ipsum dolor sit amet, consetetur sadipscing elitr, sed diam nonumy eirmod tempor.</p></div>
  </div>
  <div class="photo" role="img" aria-label="Team meeting at a whiteboard in a bright office" style="left:348px;top:62px;width:206px;height:206px;background:linear-gradient(135deg,#d9d3c8,#8f7f6e)"></div>
  <div class="brand-stack">Bright<br>Towns<br>Alliance</div><div class="brand-dot"></div>
</section>

<!-- 4 Section divider -->
<section class="slide col-b dark" style="top:388px">
  <div class="photo" role="img" aria-label="Architectural plans rolled on a desk" style="left:290px;top:28px;width:238px;height:238px;background:linear-gradient(135deg,#dfe5ee,#9aa9bf);box-shadow:0 2px 6px rgba(0,0,0,.3)"></div>
  <div class="abs orange-title" style="left:106px;top:82px;width:170px">Lorem Ipsum Dolor Sit Amet</div>
  <p class="abs body-text" style="left:106px;top:160px;width:170px">Lorem ipsum dolor sit amet, consetetur sadipscing elitr, sed diam nonumy eirmod tempor invidunt ut labore et dolore magna.</p>
  <div class="brand-stack">Bright<br>Towns<br>Alliance</div>
</section>

<!-- 5 Photo strip -->
<section class="slide col-a dark" style="top:742px">
  <div class="photo" role="img" aria-label="City skyline background tinted blue" style="inset:0;background:linear-gradient(180deg,#3f5f93 0%,#2c4f85 60%,#29467a 100%)"></div>
  <div class="abs" style="left:0;width:560px;top:22px;text-align:center;font-size:18px;color:var(--orange)">Lorem ipsum dolor sit amet</div>
  <p class="abs body-text" style="left:70px;top:50px;width:420px;text-align:center">Lorem ipsum dolor sit amet, consetetur sadipscing elitr, sed diam nonumy eirmod tempor invidunt ut labore et dolore magna aliquyam erat, sed diam voluptua. At vero eos et accusam et justo duo dolores et ea rebum. Stet clita kasd gubergren, no sea takimata sanctus est lorem ipsum.</p>
  <div class="abs" style="right:14px;top:12px;font-size:10px;line-height:1.05;color:#fff">Bright<br>Towns<br>Alliance</div>
  <div class="abs" style="left:40px;top:194px;display:flex;gap:62px">
    <div><div class="photo" role="img" aria-label="Grayscale office tower" style="position:relative;width:66px;height:72px;background:linear-gradient(#e4e4e4,#6c6c6c)"></div><div class="caption" style="color:#fff;margin-top:10px">Lorem ipsum</div></div>
    <div><div class="photo" role="img" aria-label="Grayscale glass facade" style="position:relative;width:66px;height:72px;background:linear-gradient(#d6d6d6,#555)"></div><div class="caption" style="color:#fff;margin-top:10px">Lorem ipsum</div></div>
    <div><div class="photo" role="img" aria-label="Grayscale street scene" style="position:relative;width:66px;height:72px;background:linear-gradient(#cfcfcf,#3c3c3c)"></div><div class="caption" style="color:#fff;margin-top:10px">Lorem ipsum</div></div>
    <div><div class="photo" role="img" aria-label="Grayscale skyscrapers" style="position:relative;width:66px;height:72px;background:linear-gradient(#e0e0e0,#666)"></div><div class="caption" style="color:#fff;margin-top:10px">Lorem ipsum</div></div>
  </div>
</section>

<!-- 6 Icons process -->
<section class="slide col-b" style="top:742px">
  <div class="head" style="font-size:15px;color:var(--navy);letter-spacing:.5px"><span class="mark"></span>LOREM IPSUM</div>
  <p class="abs body-text" style="left:26px;top:46px;width:510px">Lorem ipsum dolor sit amet, consetetur sadipscing elitr, sed diam nonumy eirmod tempor invidunt ut labore et dolore magna aliquyam erat, sed diam voluptua. At vero eos et accusam et justo duo dolores et ea rebum. Stet clita kasd gubergren, no sea takimata sanctus est lorem ipsum dolor sit amet.</p>
  <svg class="abs" style="left:0;top:110px" width="560" height="70" viewBox="0 0 560 70">
    <line x1="50" y1="50" x2="520" y2="50" stroke="#c9d3e3" stroke-width="1"/>
    <rect x="97" y="47" width="6" height="6" fill="#1c3468"/><rect x="277" y="47" width="6" height="6" fill="#1c3468"/><rect x="447" y="47" width="6" height="6" fill="#1c3468"/>
    <g fill="none" stroke="#1c3468" stroke-width="2"><line x1="86" y1="28" x2="114" y2="28"/><rect x="90" y="14" width="4" height="14" fill="#1c3468"/><rect x="98" y="8" width="4" height="20" fill="#1c3468"/><rect x="106" y="18" width="4" height="10" fill="#1c3468"/></g>
    <path d="M280 6 L294 11 V20 C294 27 288 31 280 34 C272 31 266 27 266 20 V11 Z" fill="#1c3468"/>
    <circle cx="450" cy="20" r="7" fill="none" stroke="#2a66d0" stroke-width="4" stroke-dasharray="3 2.5"/><circle cx="460" cy="30" r="3" fill="#2a66d0"/>
  </svg>
  <div class="abs" style="left:40px;top:170px;width:500px;display:flex;justify-content:space-between;text-align:center">
    <div style="width:120px"><div style="font-size:7px;color:var(--navy)">Lorem ipsum<br>dolor sit amet</div><p class="body-text" style="margin-top:4px">Lorem ipsum dolor sit amet, consetetur sadipscing elitr, sed diam nonumy.</p></div>
    <div style="width:120px"><div style="font-size:7px;color:var(--navy)">Lorem ipsum<br>dolor sit amet</div><p class="body-text" style="margin-top:4px">Lorem ipsum dolor sit amet, consetetur sadipscing elitr, sed diam nonumy.</p></div>
    <div style="width:120px"><div style="font-size:7px;color:var(--navy)">Lorem ipsum<br>dolor sit amet</div><p class="body-text" style="margin-top:4px">Lorem ipsum dolor sit amet, consetetur sadipscing elitr, sed diam nonumy.</p></div>
  </div>
  <div class="brand-dot"></div>
</section>

<!-- 7 Three photos -->
<section class="slide col-a" style="top:1092px">
  <div class="head"><span class="mark"></span>Lorem ipsum</div>
  <svg class="abs" style="left:0;top:44px" width="560" height="20" viewBox="0 0 560 20"><line x1="30" y1="10" x2="530" y2="10" stroke="#c9d3e3"/><rect x="97" y="7" width="6" height="6" fill="#1c3468"/><rect x="277" y="7" width="6" height="6" fill="#1c3468"/><rect x="447" y="7" width="6" height="6" fill="#1c3468"/></svg>
  <div class="abs" style="left:20px;top:68px;width:520px;display:flex;justify-content:space-between">
    <div style="width:148px"><div class="caption">Lorem ipsum dolor sit amet</div><div class="photo" role="img" aria-label="Technician working on machinery" style="position:relative;margin-top:16px;width:148px;height:66px;background:linear-gradient(135deg,#8aa0b8,#3d5470)"></div><p class="body-text" style="margin-top:8px">Lorem ipsum dolor sit amet, consetetur sadipscing elitr, sed diam nonumy eirmod tempor invidunt ut labore et dolore magna aliquyam erat, sed diam voluptua.</p></div>
    <div style="width:148px"><div class="caption">Lorem ipsum dolor sit amet</div><div class="photo" role="img" aria-label="Hands assembling electronic parts" style="position:relative;margin-top:16px;width:148px;height:66px;background:linear-gradient(135deg,#d3d7c6,#8b8f78)"></div><p class="body-text" style="margin-top:8px">Lorem ipsum dolor sit amet, consetetur sadipscing elitr, sed diam nonumy eirmod tempor invidunt ut labore et dolore magna aliquyam erat, sed diam voluptua.</p></div>
    <div style="width:148px"><div class="caption">Lorem ipsum dolor sit amet</div><div class="photo" role="img" aria-label="Close view of engine gears" style="position:relative;margin-top:16px;width:148px;height:66px;background:linear-gradient(135deg,#a9a9a9,#3e3e3e)"></div><p class="body-text" style="margin-top:8px">Lorem ipsum dolor sit amet, consetetur sadipscing elitr, sed diam nonumy eirmod tempor invidunt ut labore et dolore magna aliquyam erat, sed diam voluptua.</p></div>
  </div>
  <div class="brand-stack">Bright<br>Towns<br>Alliance</div><div class="brand-dot"></div>
</section>

<!-- 8 Section with side photos -->
<section class="slide col-b dark" style="top:1092px">
  <div class="photo" role="img" aria-label="Engineer in hard hat tinted blue" style="inset:0;background:linear-gradient(120deg,#4a6aa0,#2e4c80)"></div>
  <div class="abs orange-title" style="left:90px;top:106px;width:180px">Lorem Ipsum Dolor Sit Amet</div>
  <p class="abs body-text" style="left:90px;top:174px;width:180px">Lorem ipsum dolor sit amet, consetetur sadipscing elitr, sed diam nonumy eirmod tempor invidunt ut labore et dolore magna aliquyam erat.</p>
  <div class="abs" style="left:362px;top:40px;display:flex;flex-direction:column;gap:16px">
    <div style="display:flex;gap:8px;align-items:flex-start"><div style="width:110px"><div style="font-size:6px;color:var(--orange);text-align:right">Lorem ipsum dolor</div><p class="body-text" style="text-align:right;margin-top:3px">Lorem ipsum dolor sit amet, sadipscing elitr sed diam.</p></div><div class="photo" role="img" aria-label="Worker with tablet" style="position:relative;width:62px;height:62px;background:linear-gradient(135deg,#cfd8e4,#6e84a4)"></div></div>
    <div style="display:flex;gap:8px;align-items:flex-start"><div style="width:110px"><div style="font-size:6px;color:var(--orange);text-align:right">Lorem ipsum dolor</div><p class="body-text" style="text-align:right;margin-top:3px">Lorem ipsum dolor sit amet, sadipscing elitr sed diam.</p></div><div class="photo" role="img" aria-label="Engineers in a plant" style="position:relative;width:62px;height:62px;background:linear-gradient(135deg,#3f6fc0,#1a2f5c)"></div></div>
    <div style="display:flex;gap:8px;align-items:flex-start"><div style="width:110px"><div style="font-size:6px;color:var(--orange);text-align:right">Lorem ipsum dolor</div><p class="body-text" style="text-align:right;margin-top:3px">Lorem ipsum dolor sit amet, sadipscing elitr sed diam.</p></div><div class="photo" role="img" aria-label="Technicians at a control panel" style="position:relative;width:62px;height:62px;background:linear-gradient(135deg,#3a5fa8,#13244a)"></div></div>
  </div>
  <div class="brand-stack">Bright<br>Towns<br>Alliance</div>
</section>

<!-- 9 Timeline A -->
<section class="slide col-a" style="top:1444px">
  <div class="head"><span class="mark"></span>Lorem ipsum</div>
  <p class="abs body-text" style="left:170px;top:22px;width:370px">Lorem ipsum dolor sit amet, consetetur sadipscing elitr, sed diam nonumy eirmod tempor invidunt ut labore et dolore magna aliquyam erat, sed diam voluptua. At vero eos et accusam et justo duo dolores et ea rebum. Stet clita kasd gubergren, no sea takimata sanctus est.</p>
  <div class="timeline-year" style="left:42px;top:122px">2011</div><div class="timeline-year" style="left:156px;top:122px">2012</div><div class="timeline-year" style="left:270px;top:122px">2013</div><div class="timeline-year" style="left:384px;top:122px">2014</div>
  <div class="abs" style="left:30px;top:150px;width:500px;height:1px;background:var(--navy)"></div>
  <div class="abs" style="left:34px;top:174px;width:460px;display:flex;justify-content:space-between;text-align:center">
    <p class="body-text" style="width:76px">Lorem ipsum dolor sit amet, sadipscing elitr, sed diam nonumy eirmod tempor.</p><p class="body-text" style="width:76px">Lorem ipsum dolor sit amet, sadipscing elitr, sed diam nonumy eirmod tempor.</p><p class="body-text" style="width:76px">Lorem ipsum dolor sit amet, sadipscing elitr, sed diam nonumy eirmod tempor.</p><p class="body-text" style="width:76px">Lorem ipsum dolor sit amet, sadipscing elitr, sed diam nonumy eirmod tempor.</p>
  </div>
  <div class="brand-stack">Bright<br>Towns<br>Alliance</div><div class="brand-dot"></div>
</section>

<!-- 10 Timeline B -->
<section class="slide col-b" style="top:1444px">
  <div class="head"><span class="mark"></span>Lorem ipsum</div>
  <p class="abs body-text" style="left:170px;top:22px;width:370px">Lorem ipsum dolor sit amet, consetetur sadipscing elitr, sed diam nonumy eirmod tempor invidunt ut labore et dolore magna aliquyam erat, sed diam voluptua. At vero eos et accusam et justo duo dolores et ea rebum. Stet clita kasd gubergren, no sea takimata sanctus est.</p>
  <div class="timeline-year" style="left:100px;top:122px">2015</div><div class="timeline-year" style="left:214px;top:122px">2016</div><div class="timeline-year" style="left:328px;top:122px">2017</div><div class="timeline-year" style="left:442px;top:122px">2018</div>
  <div class="abs" style="left:30px;top:150px;width:500px;height:1px;background:var(--navy)"></div>
  <div class="abs" style="left:92px;top:174px;width:460px;display:flex;justify-content:space-between;text-align:center">
    <p class="body-text" style="width:76px">Lorem ipsum dolor sit amet, sadipscing elitr, sed diam nonumy eirmod tempor.</p><p class="body-text" style="width:76px">Lorem ipsum dolor sit amet, sadipscing elitr, sed diam nonumy eirmod tempor.</p><p class="body-text" style="width:76px">Lorem ipsum dolor sit amet, sadipscing elitr, sed diam nonumy eirmod tempor.</p><p class="body-text" style="width:76px">Lorem ipsum dolor sit amet, sadipscing elitr, sed diam nonumy eirmod tempor.</p>
  </div>
  <div class="brand-stack">Bright<br>Towns<br>Alliance</div><div class="brand-dot"></div>
</section>

<!-- 11 Bar chart -->
<section class="slide col-a dark" style="top:1800px">
  <div class="photo" role="img" aria-label="Business handshake over a desk tinted blue" style="inset:0;background:linear-gradient(120deg,#4b6a9e,#2c4a7e)"></div>
  <div class="abs" style="left:14px;top:12px;font-size:15px;line-height:1.05;color:#fff">Bright<br>Towns<br>Alliance</div>
  <div class="abs orange-title" style="right:40px;top:30px;width:180px;text-align:right">Lorem Ipsum Dolor Sit Amet</div>
  <div class="abs" style="left:30px;top:208px;width:110px"><div style="font-size:6.5px;color:#fff">Lorem ipsum Dolor</div><p class="body-text" style="margin-top:3px">Lorem ipsum dolor sit amet, consetetur sadipscing elitr, sed diam nonumy eirmod tempor invidunt ut labore et dolore.</p></div>
  <svg class="abs" style="left:160px;top:30px" width="180" height="260" viewBox="0 0 180 260" font-family="Questrial, Arial, sans-serif">
    <g fill="#f28a1e">
      <rect x="16" y="180" width="14" height="60"/><rect x="36" y="148" width="14" height="92"/><rect x="56" y="16" width="14" height="224"/><rect x="76" y="82" width="14" height="158"/><rect x="96" y="121" width="14" height="119"/><rect x="116" y="86" width="14" height="154"/><rect x="136" y="79" width="14" height="161"/>
    </g>
    <g fill="#fff" font-size="7" text-anchor="middle">
      <text x="23" y="176">17</text><text x="43" y="144">26</text><text x="63" y="12">64</text><text x="83" y="78">45</text><text x="103" y="117">34</text><text x="123" y="82">44</text><text x="143" y="75">46</text>
    </g>
    <line x1="10" y1="240" x2="156" y2="240" stroke="#c9d3e3" stroke-width=".8"/>
    <g fill="#dbe4f3" font-size="4.5" text-anchor="middle"><text x="23" y="249">Item</text><text x="43" y="249">Item</text><text x="63" y="249">Item</text><text x="83" y="249">Item</text><text x="103" y="249">Item</text><text x="123" y="249">Item</text><text x="143" y="249">Item</text></g>
  </svg>
</section>

<!-- 12 Team -->
<section class="slide col-b" style="top:1800px">
  <div class="head"><span class="mark"></span>Lorem ipsum</div>
  <div class="abs" style="left:84px;top:82px;width:400px;display:flex;justify-content:space-between;text-align:center">
    <div style="width:82px"><div class="photo" role="img" aria-label="Portrait of team member" style="position:relative;margin:0 auto;width:42px;height:44px;background:linear-gradient(#e6e8ec,#9aa3b0);border:1px solid #cfd5de"></div><div style="font-size:7px;color:var(--navy);margin-top:8px">Lorem Ipsum</div><div class="body-text" style="color:var(--muted)">Lorem dolor amet</div><p class="body-text" style="margin-top:4px">Lorem ipsum dolor sit amet, consetetur sadipscing elitr sed diam.</p><div class="social" style="margin-top:10px"><span></span><span></span><span></span><span></span></div></div>
    <div style="width:82px"><div class="photo" role="img" aria-label="Portrait of team member" style="position:relative;margin:0 auto;width:42px;height:44px;background:linear-gradient(#e6e8ec,#9aa3b0);border:1px solid #cfd5de"></div><div style="font-size:7px;color:var(--navy);margin-top:8px">Lorem Ipsum</div><div class="body-text" style="color:var(--muted)">Lorem dolor amet</div><p class="body-text" style="margin-top:4px">Lorem ipsum dolor sit amet, consetetur sadipscing elitr sed diam.</p><div class="social" style="margin-top:10px"><span></span><span></span><span></span><span></span></div></div>
    <div style="width:82px"><div class="photo" role="img" aria-label="Portrait of team member" style="position:relative;margin:0 auto;width:42px;height:44px;background:linear-gradient(#e6e8ec,#9aa3b0);border:1px solid #cfd5de"></div><div style="font-size:7px;color:var(--navy);margin-top:8px">Lorem Ipsum</div><div class="body-text" style="color:var(--muted)">Lorem dolor amet</div><p class="body-text" style="margin-top:4px">Lorem ipsum dolor sit amet, consetetur sadipscing elitr sed diam.</p><div class="social" style="margin-top:10px"><span></span><span></span><span></span><span></span></div></div>
    <div style="width:82px"><div class="photo" role="img" aria-label="Portrait of team member" style="position:relative;margin:0 auto;width:42px;height:44px;background:linear-gradient(#e6e8ec,#9aa3b0);border:1px solid #cfd5de"></div><div style="font-size:7px;color:var(--navy);margin-top:8px">Lorem Ipsum</div><div class="body-text" style="color:var(--muted)">Lorem dolor amet</div><p class="body-text" style="margin-top:4px">Lorem ipsum dolor sit amet, consetetur sadipscing elitr sed diam.</p><div class="social" style="margin-top:10px"><span></span><span></span><span></span><span></span></div></div>
  </div>
  <div class="brand-stack">Bright<br>Towns<br>Alliance</div><div class="brand-dot"></div>
</section>

<!-- 13 Line chart -->
<section class="slide col-a" style="top:2152px">
  <div class="head"><span class="mark"></span>Lorem ipsum</div>
  <p class="abs body-text" style="left:26px;top:148px;width:150px">Lorem ipsum dolor sit amet, consetetur sadipscing elitr, sed diam nonumy eirmod tempor invidunt ut labore et dolore magna aliquyam erat, sed diam voluptua. At vero eos et accusam et justo duo dolores et ea rebum.</p>
  <svg class="abs" style="left:200px;top:22px" width="350" height="230" viewBox="0 0 350 230" font-family="Questrial, Arial, sans-serif">
    <text x="22" y="14" font-size="7" fill="#1c3468">Lorem ipsum</text>
    <g stroke="#e3e8f0" stroke-width=".8"><line x1="20" y1="30" x2="340" y2="30"/><line x1="20" y1="70" x2="340" y2="70"/><line x1="20" y1="110" x2="340" y2="110"/><line x1="20" y1="150" x2="340" y2="150"/><line x1="20" y1="190" x2="340" y2="190"/></g>
    <line x1="20" y1="24" x2="20" y2="190" stroke="#c9d3e3"/>
    <polyline fill="none" stroke="#1c3468" stroke-width="1.5" points="36,172 60,152 84,100 108,72 132,88 156,92 180,96 204,106 228,108 252,126 276,100 300,98"/>
    <g fill="#fff" stroke="#1c3468" stroke-width="1"><circle cx="36" cy="172" r="2"/><circle cx="60" cy="152" r="2"/><circle cx="84" cy="100" r="2"/><circle cx="108" cy="72" r="2"/><circle cx="132" cy="88" r="2"/><circle cx="156" cy="92" r="2"/><circle cx="180" cy="96" r="2"/><circle cx="204" cy="106" r="2"/><circle cx="228" cy="108" r="2"/><circle cx="252" cy="126" r="2"/><circle cx="276" cy="100" r="2"/><circle cx="300" cy="98" r="2"/></g>
    <g fill="#8a8f99" font-size="4.5" text-anchor="middle"><text x="36" y="200">Item</text><text x="60" y="200">Item</text><text x="84" y="200">Item</text><text x="108" y="200">Item</text><text x="132" y="200">Item</text><text x="156" y="200">Item</text><text x="180" y="200">Item</text><text x="204" y="200">Item</text><text x="228" y="200">Item</text><text x="252" y="200">Item</text><text x="276" y="200">Item</text><text x="300" y="200">Item</text></g>
    <g fill="#8a8f99" font-size="4.5" text-anchor="end"><text x="16" y="32">50</text><text x="16" y="72">40</text><text x="16" y="112">30</text><text x="16" y="152">20</text><text x="16" y="192">10</text></g>
  </svg>
  <div class="brand-stack">Bright<br>Towns<br>Alliance</div>
</section>

<!-- 14 Donut charts -->
<section class="slide col-b dark" style="top:2152px">
  <div class="photo" role="img" aria-label="City skyline at night tinted deep blue" style="inset:0;background:linear-gradient(180deg,#30528f,#1d3872)"></div>
  <div class="abs" style="left:0;width:560px;top:14px;text-align:center;font-size:16px;color:var(--orange)">Lorem ipsum dolor sit amet</div>
  <p class="abs body-text" style="left:30px;top:38px;width:500px">Lorem ipsum dolor sit amet, consetetur sadipscing elitr, sed diam nonumy eirmod tempor invidunt ut labore et dolore magna aliquyam erat, sed diam voluptua. At vero eos et accusam et justo duo dolores et ea rebum. Stet clita kasd gubergren, no sea takimata sanctus est lorem ipsum dolor sit amet.</p>
  <svg class="abs" style="left:0;top:0" width="560" height="314" viewBox="0 0 560 314" font-family="Questrial, Arial, sans-serif">
    <circle cx="202" cy="152" r="50" fill="none" stroke="rgba(255,255,255,.25)" stroke-width="14"/>
    <circle cx="202" cy="152" r="50" fill="none" stroke="#f28a1e" stroke-width="14" stroke-dasharray="241.9 314.2" transform="rotate(-90 202 152)"/>
    <text x="202" y="136" font-size="6" fill="#fff" text-anchor="middle">Text</text>
    <text x="202" y="163" font-size="24" fill="#f28a1e" text-anchor="middle">77%</text>
    <circle cx="352" cy="152" r="50" fill="none" stroke="rgba(255,255,255,.25)" stroke-width="14"/>
    <circle cx="352" cy="152" r="50" fill="none" stroke="#f28a1e" stroke-width="14" stroke-dasharray="267.1 314.2" transform="rotate(-90 352 152)"/>
    <text x="352" y="136" font-size="6" fill="#fff" text-anchor="middle">Text</text>
    <text x="352" y="163" font-size="24" fill="#f28a1e" text-anchor="middle">85%</text>
  </svg>
  <div class="brand-stack">Bright<br>Towns<br>Alliance</div>
</section>

<!-- 15 Closing -->
<section class="slide" style="top:2504px;left:332px;height:316px;background:linear-gradient(180deg,#c9d2de 0%,#9fb0c6 45%,#5a77a6 62%,#3d5f96 100%)">
  <div class="photo" role="img" aria-label="Smiling businessman in a suit with arms crossed" style="left:370px;top:14px;width:170px;height:302px;background:linear-gradient(180deg,#d8c7b4 0%,#3a4660 40%,#1f2a44 100%)"></div>
  <div class="abs" style="left:36px;top:112px;font-size:27px;color:#fff">Bright Towns Alliance</div>
  <div class="abs body-text" style="left:38px;top:206px;width:150px;color:#fff;font-size:6px;line-height:1.6">
    <div style="color:var(--orange);font-size:7px">Lorem Ipsum Dolor</div>
    +1 555 0142 786<br>contact@brighttowns-example.org<br>1200 Lorem Street, Suite 10<br>Demo City, DC 00000<br>www.brighttowns-example.org
  </div>
  <div class="abs" style="left:208px;top:222px;display:flex;gap:12px">
    <span style="width:28px;height:28px;background:var(--orange)"></span><span style="width:28px;height:28px;background:var(--orange)"></span><span style="width:28px;height:28px;background:var(--orange)"></span>
  </div>
</section>

</body>
</html>
```